Financial industry/Advisor business card

I'm a Financial Advisor starting my own investment company, Brantley Wealth Management. I currently use the 'Light Blue' color that's provided on the Cardwise web page, but I want something unique. I'd like to keep the color, but the design is up for grabs.

Industry/Entity Type

Business

Contact Information for Business Card

Brantley Wealth Management
Dean R. Brantley
President
5129 Willowgate Ln
Ste 240
Ashbury Vale Nc 28406
555-372-6140-Office
555-372-6187-Fax
DBRANTLEY@BRANTWM.example

```html
<!DOCTYPE html>
<html lang="en">
<head>
<meta charset="utf-8">
<title>Brantley Wealth Management – Business Card</title>
<link href="https://fonts.googleapis.com/css2?family=Old+Standard+TT:wght@400;700&display=swap" rel="stylesheet">
<style>
  :root {
    --brand-teal: #005c7b;
    --ink-teal: #0d5676;
    --paper: #ffffff;
    --backdrop: #e9ecee;
    --card-shadow: rgba(0, 0, 0, 0.18);
  }
  * { margin: 0; padding: 0; box-sizing: border-box; }
  html, body {
    width: 1200px; height: 800px; overflow: hidden;
    background: var(--backdrop);
    font-family: "Old Standard TT", "Times New Roman", serif;
  }
  .canvas {
    position: relative; width: 1200px; height: 800px;
    display: flex; flex-direction: column; align-items: center; justify-content: center;
    gap: 44px;
  }
  .card {
    position: relative; width: 600px; height: 343px;
    box-shadow: 0 10px 28px var(--card-shadow);
  }
  .card--back {
    background: var(--brand-teal);
    color: var(--paper);
    display: flex; flex-direction: column; align-items: center; justify-content: center;
    gap: 14px;
  }
  .brand-mark {
    width: 70px; height: 70px;
    border: 4px solid currentColor; border-radius: 10px;
  }
  .brand-name { font-weight: 700; font-size: 25px; letter-spacing: 0.5px; }
  .card--front { background: var(--paper); color: var(--ink-teal); }
  .front-brand {
    position: absolute; top: 32px; left: 150px; right: 60px;
    display: flex; flex-direction: column; align-items: center; gap: 10px;
  }
  .front-brand .brand-mark { width: 76px; height: 76px; }
  .front-brand .brand-name { font-size: 26px; }
  .person {
    position: absolute; left: 42px; top: 176px; width: 500px;
    padding-bottom: 4px;
    border-bottom: 2px solid var(--ink-teal);
    font-size: 19px;
  }
  .person-name { letter-spacing: 0.6px; }
  .person-divider { margin: 0 14px; }
  .person-title { font-size: 16px; }
  .contact-list {
    position: absolute; left: 28px; top: 214px;
    list-style: none; font-size: 17px;
    display: flex; flex-direction: column; gap: 3px;
  }
  .contact-item { display: flex; align-items: center; gap: 10px; }
  .contact-icon { width: 15px; height: 15px; fill: var(--ink-teal); flex: none; }
  .address {
    position: absolute; right: 40px; top: 288px;
    font-style: normal; font-size: 17px; text-align: right; line-height: 1.3;
  }
</style>
</head>
<body>
<main class="canvas">
  <section class="card card--back" aria-label="Card back">
    <div class="brand-mark" aria-hidden="true"></div>
    <p class="brand-name">Brantley Wealth Management</p>
  </section>

  <section class="card card--front" aria-label="Card front">
    <div class="front-brand">
      <div class="brand-mark" aria-hidden="true"></div>
      <p class="brand-name">Brantley Wealth Management</p>
    </div>

    <p class="person">
      <span class="person-name">DEAN R. BRANTLEY</span><span class="person-divider">|</span><span class="person-title">President</span>
    </p>

    <ul class="contact-list">
      <li class="contact-item">
        <svg class="contact-icon" viewBox="0 0 24 24" aria-label="Office phone"><path d="M6.6 10.8c1.4 2.8 3.8 5.1 6.6 6.6l2.2-2.2c.3-.3.7-.4 1-.2 1.1.4 2.3.6 3.6.6.6 0 1 .4 1 1V20c0 .6-.4 1-1 1C10.6 21 3 13.4 3 4c0-.6.4-1 1-1h3.5c.6 0 1 .4 1 1 0 1.3.2 2.5.6 3.6.1.3 0 .7-.2 1z"/></svg>
        <span>555-372-6140</span>
      </li>
      <li class="contact-item">
        <svg class="contact-icon" viewBox="0 0 24 24" aria-label="Fax"><path d="M7 2h10v5H7zM4 8h16a2 2 0 0 1 2 2v7h-4v5H6v-5H2v-7a2 2 0 0 1 2-2zm4 9v3h8v-3z"/></svg>
        <span>555-372-6187</span>
      </li>
      <li class="contact-item">
        <svg class="contact-icon" viewBox="0 0 24 24" aria-label="Email"><path d="M2 5h20v14H2zm2 2v.5l8 5 8-5V7z"/></svg>
        <span>DBRANTLEY@BRANTWM.example</span>
      </li>
    </ul>

    <address class="address">
      5129 Willowgate Ln Ste 240<br>
      Ashbury Vale Nc 28406
    </address>
  </section>
</main>
</body>
</html>
```